App for Lawyers & Accountants needs 'Professional' Styling

We want to style our app to convey a 'Professional' appearance. It's used by Lawyers, Accountants, Doctors etc. who take their work very seriously.

We currently trying to follow keystrel layout guidelines, but we find our app looks very bland. I've uploaded a screenshot of our current app, and two mock-ups of more stylized versions, but we're not happy with those mock-ups.

We'd like to see alternate designs for those two mock-ups, that look much more professional.

The specific elements we'd like to improve/focus on are:
* Colour of the top and left nav bars
* Appearance of the left nav, size, icons spacing
* Appearance of the buttons on the top right, so the user knows they are buttons they can press
* Spacing of the dashboard, background colour and spacing, colour/layout of the 'overdue' and 'todo' accordion headings in the 'my tasks' section.
* List view background grey, to be consistent with dashboard, but unobtrusive
* List view tabs to be obvious as tabs, but 'saved searches', filters and the export icon to still be associated with the data displayed, but it should be obvious to the user that those are different buttons, not just more tabs. (I.e. the filters button opens a panel below it that allows the user to filter the data in the list.)
* General appearance of the popup menu when you push the 'add' button on the top right

However, despite those specifics I'm sure it's all the subtle elements of the design that make a big difference.

Our brand colour is 1D4F91, and we use A20067 as a secondary colour in print media, (although it doesn't seem to work to well within the app.) Our brand font is signika. We'd like the designs to be based on those colours & font.

Target Market(s)

Professional people, Lawyers, Accountants, Doctors etc.

Font styles to use
Sans Serif
Other font styles liked:
• Signika

Colors
0255a3

Requirements
Must have
• The most 'Professional' experience/quality possible. Think the quality & brand image of vantrel desk, but taken to a higher level.
• An example/mock-up of the dashboard, list view and 'add' item popup menu
• Display the dashboard cards with the same information as our mock-ups - the information there is important and we don't have any extra cards to add (in the near term)
Nice to have
• Various colour combinations for the top and left nav bars, based on our primary blue brand colour, and perhaps some shade of dark grey.

```html
<!DOCTYPE html>
<html lang="en">
<head>
<meta charset="utf-8">
<title>Corvane – My Matter</title>
<link href="https://fonts.googleapis.com/css2?family=Montserrat:wght@400;500;600;700&display=swap" rel="stylesheet">
<style>
:root{
  --stage:#cfcfcf;
  --brand:#1f4f91;
  --brand-deep:#163a6e;
  --side:#1c2433;
  --accent:#a20067;
  --page:#f8f8f8;
  --card:#ffffff;
  --row-alt:#f6f6f6;
  --line:#e6e6e6;
  --ink:#1d1d1d;
  --ink-soft:#3c3c3c;
  --muted:#6f6f6f;
  --white:#ffffff;
}
*{box-sizing:border-box;margin:0;padding:0}
html,body{width:1200px;height:768px;overflow:hidden}
body{background:var(--stage);font-family:"Montserrat",sans-serif;color:var(--ink)}
.app{position:absolute;left:13px;top:17px;width:1171px;height:731px;background:var(--page);overflow:hidden}
.topbar{position:absolute;left:0;top:0;width:100%;height:71px;background:var(--brand)}
.brand{position:absolute;left:0;top:0;width:70px;height:71px;display:flex;flex-direction:column;align-items:center;justify-content:center;gap:6px;color:var(--white)}
.brand-dot{width:22px;height:22px;border-radius:50%;background:var(--white)}
.brand-name{font-size:10px;font-weight:700}
.search{position:absolute;left:105px;top:19px;width:669px;height:32px;border-radius:3px;background:var(--brand-deep);display:flex;align-items:center;gap:10px;padding-left:10px;color:var(--white);font-size:12px;font-weight:500}
.round-btn{position:absolute;top:19px;width:36px;height:36px;border-radius:50%;background:var(--brand-deep);display:flex;align-items:center;justify-content:center}
.badge{position:absolute;right:-3px;top:-3px;width:15px;height:15px;border-radius:50%;background:#e8413a;color:var(--white);font-size:8px;font-weight:700;display:flex;align-items:center;justify-content:center}
.user{position:absolute;left:974px;top:21px;height:32px;display:flex;align-items:center;gap:10px;color:var(--white);font-size:12px;font-weight:500}
.avatar{width:32px;height:32px;border-radius:50%;background:var(--white);display:flex;align-items:center;justify-content:center}
.kebab{margin-left:8px}
.sidebar{position:absolute;left:0;top:71px;width:70px;height:660px;background:var(--side)}
.nav-new{height:79px;background:var(--accent)}
.nav-item{display:flex;flex-direction:column;align-items:center;justify-content:center;gap:6px;height:66px;color:var(--white);font-size:9px;font-weight:600;text-align:center;line-height:1.2}
.nav-new{display:flex;flex-direction:column;align-items:center;justify-content:center;gap:8px;color:var(--white);font-size:9px;font-weight:700}
.nav-item.active{background:var(--brand)}
.nav-settings{position:absolute;left:0;bottom:14px;width:70px;height:auto}
.tabs{position:absolute;left:90px;top:93px;display:flex;height:41px;background:var(--card);box-shadow:0 1px 3px rgba(0,0,0,.15)}
.tab{display:flex;align-items:center;padding:0 26px;font-size:12.5px;font-weight:500;color:var(--ink-soft)}
.tab.current{background:var(--accent);color:var(--white);padding:0 24px}
.filters{position:absolute;left:1030px;top:93px;width:118px;height:41px;background:var(--accent);color:var(--white);display:flex;align-items:center;padding:0 13px 0 16px;gap:8px;font-size:12.5px;font-weight:600;box-shadow:0 1px 3px rgba(0,0,0,.2)}
.filters .sort{margin-left:auto}
.matters{position:absolute;left:92px;top:149px;width:1057px;height:538px;background:var(--card);box-shadow:0 1px 3px rgba(0,0,0,.12)}
.matter-table{width:100%;border-collapse:collapse;table-layout:fixed;font-size:11.5px}
.matter-table th{height:52px;text-align:left;font-weight:600;font-size:12px;color:var(--ink);border-bottom:1px solid var(--line)}
.matter-table td{height:39.4px;color:var(--ink-soft);font-weight:500}
.matter-table tbody tr:nth-child(odd){background:var(--row-alt)}
.col-title{width:385px;padding-left:34px}
.col-client{width:122px}
.col-area{width:158px}
.col-type{width:124px}
.col-updated{width:151px}
.matter-table td.col-client,.matter-table td.col-area,.matter-table td.col-type,.matter-table td.col-updated{padding-left:2px}
.col-action{padding-left:0}
td.col-action{padding-left:0;text-align:left}
td.col-action svg{margin-left:26px;display:block}
.table-foot{position:absolute;left:0;bottom:0;width:100%;height:46px;border-top:1px solid var(--line);display:flex;align-items:center;padding:0 22px 0 19px;font-size:10px;color:var(--muted)}
.table-foot b{color:var(--ink-soft);font-weight:600;margin:0 5px}
.pager{margin-left:auto;display:flex;align-items:center;gap:14px;font-size:12px;color:var(--muted);font-weight:500}
.pager .on{color:var(--accent);font-weight:700}
.copyright{position:absolute;right:60px;top:704px;font-size:10px;font-weight:600;color:var(--ink-soft)}
</style>
</head>
<body>
<div class="app">
  <header class="topbar">
    <div class="brand"><span class="brand-dot"></span><span class="brand-name">Corvane</span></div>
    <div class="search">
      <svg width="16" height="16" viewBox="0 0 16 16" fill="none" stroke="#fff" stroke-width="1.8"><circle cx="7" cy="7" r="5.5"/><path d="M11 11l4 4"/></svg>
      Search
    </div>
    <div class="round-btn" style="left:833px">
      <svg width="20" height="20" viewBox="0 0 20 20" fill="none" stroke="#fff" stroke-width="2"><path d="M4 10a6 6 0 1 0 1.8-4.3"/><path d="M3 4v4h4"/><path d="M10 6.5V10l2.5 2"/></svg>
    </div>
    <div class="round-btn" style="left:897px">
      <svg width="20" height="20" viewBox="0 0 20 20" fill="none" stroke="#fff" stroke-width="1.8"><path d="M5 14V9a5 5 0 0 1 10 0v5l1.5 1.5h-13z"/><path d="M8.5 17.5h3"/></svg>
      <span class="badge">5</span>
    </div>
    <div class="user">
      Daniel Reyes
      <span class="avatar"><svg width="20" height="20" viewBox="0 0 20 20" fill="#9a9a9a"><circle cx="10" cy="7" r="4"/><path d="M2 18c1-4 4.5-6 8-6s7 2 8 6z"/></svg></span>
      <svg class="kebab" width="4" height="16" viewBox="0 0 4 16" fill="#fff"><circle cx="2" cy="2" r="2"/><circle cx="2" cy="8" r="2"/><circle cx="2" cy="14" r="2"/></svg>
    </div>
  </header>

  <nav class="sidebar">
    <div class="nav-new">
      <svg width="22" height="22" viewBox="0 0 22 22"><circle cx="11" cy="11" r="10.5" fill="#fff"/><path d="M11 6v10M6 11h10" stroke="#a20067" stroke-width="3"/></svg>
      NEW
    </div>
    <div class="nav-item active">
      <svg width="15" height="13" viewBox="0 0 15 13" fill="#fff"><rect x="0" y="0" width="4" height="3.5"/><rect x="5.5" y="0" width="4" height="3.5"/><rect x="11" y="0" width="4" height="3.5"/><rect x="0" y="4.7" width="4" height="3.5"/><rect x="5.5" y="4.7" width="4" height="3.5"/><rect x="11" y="4.7" width="4" height="3.5"/><rect x="0" y="9.4" width="4" height="3.5"/><rect x="5.5" y="9.4" width="4" height="3.5"/><rect x="11" y="9.4" width="4" height="3.5"/></svg>
      Dashboard
    </div>
    <div class="nav-item">
      <svg width="18" height="18" viewBox="0 0 18 18" fill="#4f8fd9"><rect x="4" y="2" width="8" height="5" rx="1" transform="rotate(45 8 4.5)"/><rect x="9" y="8" width="3" height="10" transform="rotate(-45 10.5 13)"/></svg>
      Matter
    </div>
    <div class="nav-item">
      <svg width="16" height="17" viewBox="0 0 16 17" fill="none" stroke="#4f8fd9" stroke-width="1.7"><circle cx="8" cy="5.5" r="4"/><path d="M1 16c0-3.5 3-5.5 7-5.5s7 2 7 5.5z"/></svg>
      Contact
    </div>
    <div class="nav-item">
      <svg width="17" height="19" viewBox="0 0 17 19" fill="#4f8fd9"><rect x="5" y="0" width="11" height="14" rx="1"/><rect x="1" y="4" width="11" height="14" rx="1" stroke="#1c2433" stroke-width="1.5"/></svg>
      Document
    </div>
    <div class="nav-item">
      <svg width="18" height="15" viewBox="0 0 18 15" fill="none" stroke="#4f8fd9" stroke-width="1.8"><path d="M1 2l1.5 1.5L5 1M1 7.5l1.5 1.5L5 6.5"/><path d="M7 2.5h10M7 7.5h10M1 13h16"/></svg>
      Task
    </div>
    <div class="nav-item">
      <svg width="18" height="18" viewBox="0 0 18 18" fill="none" stroke="#4f8fd9" stroke-width="1.8"><circle cx="9" cy="9" r="7.8"/><path d="M9 4.5V9l3 2"/></svg>
      Time<br>Records
    </div>
    <div class="nav-item nav-settings">
      <svg width="20" height="20" viewBox="0 0 20 20"><g fill="#4f8fd9"><circle cx="10" cy="10" r="6.5"/><rect x="8" y="0.5" width="4" height="19" rx="1"/><rect x="8" y="0.5" width="4" height="19" rx="1" transform="rotate(60 10 10)"/><rect x="8" y="0.5" width="4" height="19" rx="1" transform="rotate(120 10 10)"/></g><circle cx="10" cy="10" r="2.6" fill="#1c2433"/></svg>
      Settings
    </div>
  </nav>

  <div class="tabs">
    <div class="tab current">My Matter</div>
    <div class="tab">Recent Matters</div>
    <div class="tab" style="padding:0 28px 0 38px">All Matters</div>
    <div class="tab" style="padding:0 26px 0 28px">Saved Searches</div>
  </div>
  <div class="filters">
    <svg width="11" height="11" viewBox="0 0 11 11" fill="#fff"><path d="M0 0h11L6.8 5v6L4.2 9.5V5z"/></svg>
    Filters
    <svg class="sort" width="9" height="13" viewBox="0 0 9 13" fill="#fff"><path d="M4.5 0L9 5H0zM4.5 13L0 8h9z"/></svg>
  </div>

  <section class="matters">
    <table class="matter-table">
      <thead>
        <tr><th class="col-title">Title</th><th class="col-client">Client</th><th class="col-area">Practice Area</th><th class="col-type">Type</th><th class="col-updated">Last Updated</th><th class="col-action">Action</th></tr>
      </thead>
      <tbody>
        <tr><td class="col-title">Hadley v. Crane concerning sale #707</td><td class="col-client">R. Ostrow</td><td class="col-area">Conveyancing</td><td class="col-type">Sign Up</td><td class="col-updated">Jan 21, 2018</td><td class="col-action"><svg width="9" height="11" viewBox="0 0 9 11" fill="#1d1d1d"><rect x="0" y="1.2" width="9" height="1.4"/><rect x="3" y="0" width="3" height="1.5"/><path d="M1 3.2h7l-.6 7.8H1.6z"/></svg></td></tr>
        <tr><td class="col-title">Hadley v. Crane concerning sale #707</td><td class="col-client">R. Ostrow</td><td class="col-area">Conveyancing</td><td class="col-type">Sign Up</td><td class="col-updated">Jan 21, 2018</td><td class="col-action"><svg width="9" height="11" viewBox="0 0 9 11" fill="#1d1d1d"><rect x="0" y="1.2" width="9" height="1.4"/><rect x="3" y="0" width="3" height="1.5"/><path d="M1 3.2h7l-.6 7.8H1.6z"/></svg></td></tr>
        <tr><td class="col-title">Hadley v. Crane concerning sale #707</td><td class="col-client">R. Ostrow</td><td class="col-area">Conveyancing</td><td class="col-type">Sign Up</td><td class="col-updated">Jan 21, 2018</td><td class="col-action"><svg width="9" height="11" viewBox="0 0 9 11" fill="#1d1d1d"><rect x="0" y="1.2" width="9" height="1.4"/><rect x="3" y="0" width="3" height="1.5"/><path d="M1 3.2h7l-.6 7.8H1.6z"/></svg></td></tr>
        <tr><td class="col-title">Hadley v. Crane concerning sale #707</td><td class="col-client">R. Ostrow</td><td class="col-area">Conveyancing</td><td class="col-type">Sign Up</td><td class="col-updated">Jan 21, 2018</td><td class="col-action"><svg width="9" height="11" viewBox="0 0 9 11" fill="#1d1d1d"><rect x="0" y="1.2" width="9" height="1.4"/><rect x="3" y="0" width="3" height="1.5"/><path d="M1 3.2h7l-.6 7.8H1.6z"/></svg></td></tr>
        <tr><td class="col-title">Hadley v. Crane concerning sale #707</td><td class="col-client">R. Ostrow</td><td class="col-area">Conveyancing</td><td class="col-type">Sign Up</td><td class="col-updated">Jan 21, 2018</td><td class="col-action"><svg width="9" height="11" viewBox="0 0 9 11" fill="#1d1d1d"><rect x="0" y="1.2" width="9" height="1.4"/><rect x="3" y="0" width="3" height="1.5"/><path d="M1 3.2h7l-.6 7.8H1.6z"/></svg></td></tr>
        <tr><td class="col-title">Hadley v. Crane concerning sale #707</td><td class="col-client">R. Ostrow</td><td class="col-area">Conveyancing</td><td class="col-type">Sign Up</td><td class="col-updated">Jan 21, 2018</td><td class="col-action"><svg width="9" height="11" viewBox="0 0 9 11" fill="#1d1d1d"><rect x="0" y="1.2" width="9" height="1.4"/><rect x="3" y="0" width="3" height="1.5"/><path d="M1 3.2h7l-.6 7.8H1.6z"/></svg></td></tr>
        <tr><td class="col-title">Hadley v. Crane concerning sale #707</td><td class="col-client">R. Ostrow</td><td class="col-area">Conveyancing</td><td class="col-type">Sign Up</td><td class="col-updated">Jan 21, 2018</td><td class="col-action"><svg width="9" height="11" viewBox="0 0 9 11" fill="#1d1d1d"><rect x="0" y="1.2" width="9" height="1.4"/><rect x="3" y="0" width="3" height="1.5"/><path d="M1 3.2h7l-.6 7.8H1.6z"/></svg></td></tr>
        <tr><td class="col-title">Hadley v. Crane concerning sale #707</td><td class="col-client">R. Ostrow</td><td class="col-area">Conveyancing</td><td class="col-type">Sign Up</td><td class="col-updated">Jan 21, 2018</td><td class="col-action"><svg width="9" height="11" viewBox="0 0 9 11" fill="#1d1d1d"><rect x="0" y="1.2" width="9" height="1.4"/><rect x="3" y="0" width="3" height="1.5"/><path d="M1 3.2h7l-.6 7.8H1.6z"/></svg></td></tr>
        <tr><td class="col-title">Hadley v. Crane concerning sale #707</td><td class="col-client">R. Ostrow</td><td class="col-area">Conveyancing</td><td class="col-type">Sign Up</td><td class="col-updated">Jan 21, 2018</td><td class="col-action"><svg width="9" height="11" viewBox="0 0 9 11" fill="#1d1d1d"><rect x="0" y="1.2" width="9" height="1.4"/><rect x="3" y="0" width="3" height="1.5"/><path d="M1 3.2h7l-.6 7.8H1.6z"/></svg></td></tr>
        <tr><td class="col-title">Hadley v. Crane concerning sale #707</td><td class="col-client">R. Ostrow</td><td class="col-area">Conveyancing</td><td class="col-type">Sign Up</td><td class="col-updated">Jan 21, 2018</td><td class="col-action"><svg width="9" height="11" viewBox="0 0 9 11" fill="#1d1d1d"><rect x="0" y="1.2" width="9" height="1.4"/><rect x="3" y="0" width="3" height="1.5"/><path d="M1 3.2h7l-.6 7.8H1.6z"/></svg></td></tr>
        <tr><td class="col-title">Hadley v. Crane concerning sale #707</td><td class="col-client">R. Ostrow</td><td class="col-area">Conveyancing</td><td class="col-type">Sign Up</td><td class="col-updated">Jan 21, 2018</td><td class="col-action"><svg width="9" height="11" viewBox="0 0 9 11" fill="#1d1d1d"><rect x="0" y="1.2" width="9" height="1.4"/><rect x="3" y="0" width="3" height="1.5"/><path d="M1 3.2h7l-.6 7.8H1.6z"/></svg></td></tr>
      </tbody>
    </table>
    <div class="table-foot">
      Showing <b>1-12</b> of <b>120</b> matter
      <div class="pager">
        <svg width="8" height="12" viewBox="0 0 8 12" fill="none" stroke="#555" stroke-width="2"><path d="M6.5 1L1.5 6l5 5"/></svg>
        <span class="on" style="margin-left:12px">1</span><span>2</span><span>3</span><span>4</span><span>5</span>
        <svg style="margin-left:12px" width="8" height="12" viewBox="0 0 8 12" fill="none" stroke="#a20067" stroke-width="2"><path d="M1.5 1l5 5-5 5"/></svg>
      </div>
    </div>
  </section>

  <footer class="copyright">Company Name © 2018</footer>
</div>
</body>
</html>
```